law firm website

We need a website for our law firm that is based in Kabul, Afghanistan. We provide legal and government affairs services for the international community. We would like to see designs that use the colors of our logo, designs that are elegant and simple, yet not boring or over the top. No law or law related symbols or pictures. We would like clocks that show times for Kabul, Dubai and Washington DC.
Updates
Reason: No designs that are up to the task as yet. Perhaps we should stop using picture of people, that obviously don't work with us, in the website. If you are to use pictures, please try using pictures of Afghanistan mountains, art, craft etc. Also, please make the clocks very small - they seem to be dominating the website. We do not sell clocks or watches - we are a law firm. Hope you all understand and thank you for your designs to date.
Deal All,
Industry/Entity Type
Government
Requirements
Must have
- our logo.
the following phrases/words in flash.
"international standards" "local expertise" "integrity" "clarity" "commitment" "Afghanistan"
clocks: kabul, dubai, washington dc
Should not have
- law related pictures
afghanistan flag colors

```html
<!DOCTYPE html>
<html lang="en">
<head>
<meta charset="utf-8">
<title>Kestrel Legal Partners</title>
<link href="https://fonts.googleapis.com/css2?family=Arimo:ital,wght@0,400;0,700;1,700&family=Cinzel:wght@400&family=Raleway:wght@400;600;700&family=Roboto+Mono:wght@500;700&family=Lato:ital,wght@1,700&display=swap" rel="stylesheet">
<style>
:root{
  --blue:#34a3dc;
  --blue-dark:#1f86bf;
  --ink:#333;
  --muted:#555;
  --logo:#7c8a9a;
  --slate:#41464f;
  --night:#1c1c1c;
  --panel:#f5f5f5;
  --quote-bg:#d9e0e7;
  --white:#fff;
}
*{box-sizing:border-box;margin:0;padding:0}
html,body{width:892px;height:1200px;overflow:hidden;background:var(--white)}
body{font-family:"Arimo",Arial,sans-serif;color:var(--ink)}
.page{position:relative;width:892px;height:1200px;overflow:hidden}
.abs{position:absolute}

/* header */
.brand{left:174px;top:28px;font-family:"Cinzel",serif;color:var(--logo);font-size:13px;line-height:13px;letter-spacing:.5px;display:flex;align-items:center;gap:10px}
.brand-mark{width:30px;height:30px;background:var(--logo);border-radius:50%}
.clocks{top:4px;width:214px}
.clock-row{display:flex;align-items:center;height:14px;font-family:"Roboto Mono",monospace;font-size:7px;color:#222}
.clock-row .flag{width:10px;height:7px;margin-right:6px}
.clock-row .city{width:52px;font-weight:700}
.clock-row .time{font-weight:500;color:#444}
.clock-icon{left:514px;top:14px}
.brace{left:543px;top:5px}
.call{left:554px;top:61px;display:flex;align-items:center;gap:7px;font-family:"Raleway",sans-serif;font-size:10px;font-weight:600;color:#333}
.call strong{font-family:"Roboto Mono",monospace;font-size:12px;letter-spacing:.5px;margin-left:6px}

/* nav */
.nav{left:0;top:88px;width:892px;height:28px;background:var(--blue);border-bottom:2px solid var(--blue-dark)}
.nav ul{list-style:none;display:flex;position:absolute;left:186px;top:0;height:27px}
.nav li{font-family:"Raleway",sans-serif;font-weight:700;font-size:8.5px;color:var(--white);padding:0 7px;line-height:27px}
.nav li.active{background:#1b1b1b}

/* hero */
.hero{left:0;top:116px;width:892px;height:295px;background:linear-gradient(180deg,#b7c4d2 0%,#a9b1b3 45%,#6b665d 75%,#3e3a35 100%)}
.hero-cta{left:468px;top:214px;width:250px;height:42px;background:rgba(60,55,50,.75);color:#eee;font-family:"Raleway",sans-serif;font-size:15px;text-align:center;line-height:42px}
.hero-caption{left:0;top:357px;width:892px;height:54px;background:rgba(20,20,20,.7);color:#f2f2f2;font-family:"Cinzel",serif;font-size:11.3px;text-align:center;line-height:19px;padding-top:8px;letter-spacing:.3px}
.hero-arrow{top:371px}

/* welcome */
.section-title{font-family:"Raleway",sans-serif;font-size:15px;font-weight:400}
.welcome-title{left:168px;top:438px;color:var(--blue)}
.welcome-box{left:167px;top:464px;width:368px;height:184px;background:var(--panel);border:1px solid #e2e2e2;padding:10px 8px;font-size:7.6px;line-height:11px;color:#333}
.welcome-box ul{list-style:none;margin-top:14px}
.welcome-box li{display:flex;gap:7px;margin-bottom:9px;align-items:flex-start}
.welcome-box li svg{flex:none;margin-top:1px}
.locations-title{left:550px;top:438px;color:#222}
.office{left:552px;top:462px;width:173px;height:131px;background:#1e1e1e;text-align:center;color:var(--blue);font-family:"Raleway",sans-serif;padding-top:25px}
.office h3{font-weight:400;font-size:15px;margin-bottom:2px}
.office p{font-size:9px;line-height:13px}
.office .pager{display:flex;justify-content:center;gap:12px;margin-top:14px}
.news{left:552px;top:598px;width:173px;height:48px;background:var(--blue);color:var(--white);text-align:center;font-family:"Raleway",sans-serif;padding-top:8px}
.news h3{font-weight:400;font-size:16px}
.news span{display:block;font-size:7px;letter-spacing:3px;margin-top:1px}

/* practice */
.practice{left:0;top:672px;width:892px;height:270px;background:var(--slate)}
.practice-title{left:167px;top:690px;color:#f1f1f1}
.card{top:760px;width:137px;height:144px;background:linear-gradient(180deg,#f4f4f4 0%,#cfcfcf 100%);text-align:center;padding-top:52px}
.card h4{font-family:"Raleway",sans-serif;font-weight:400;font-size:12px;color:#333;padding-bottom:8px;border-bottom:1px solid #b5b5b5;margin:0 7px}
.card p{font-size:7.6px;line-height:9.5px;font-weight:700;color:#444;text-align:justify;padding:6px 7px 0}
.card-icon{top:722px;width:76px;height:76px}
.more{top:906px;width:61px;height:15px;background:var(--blue);color:var(--white);font-size:7.6px;font-weight:700;line-height:15px;padding-left:7px}

/* testimonials */
.testi-title{left:167px;top:958px;color:#333}
.testi{left:167px;top:986px;width:557px;height:94px;background:var(--quote-bg)}
.testi-quote{left:176px;top:996px;font-family:"Lato",serif;font-size:26px;font-style:italic;font-weight:700;color:#333}
.testi-body{left:196px;top:1004px;width:336px;font-family:"Lato",sans-serif;font-style:italic;font-weight:700;font-size:8.8px;line-height:12px;color:#333}
.testi-body .by{margin-top:12px}
.testi-body .name{font-size:7.6px;margin-top:3px}
.testi-side{left:537px;top:986px;width:187px;height:94px;background:#f0f2f4;font-size:7.8px;line-height:10px;color:#333;padding:5px 6px}
.testi-side a{color:var(--blue-dark);font-weight:700;font-style:italic;text-decoration:none}

/* footer */
.foot-nav{left:0;top:1093px;width:892px;height:28px;background:var(--blue)}
.foot-nav ul{list-style:none;display:flex;position:absolute;left:168px;top:0;gap:11px}
.foot-nav li{color:var(--white);font-size:9px;line-height:28px}
.social{left:626px;top:1097px;display:flex;gap:6px}
.social span{width:19px;height:19px;border-radius:50%;background:var(--white);display:block}
.footer{left:0;top:1121px;width:892px;height:79px;background:var(--night)}
.legal{left:167px;top:1134px;width:214px;height:18px;background:#5a5f66;color:#eee;font-size:7.6px;line-height:18px;padding-left:16px}
.copy{left:167px;top:1164px;width:560px;color:#eee;font-size:7.6px;line-height:10px}
</style>
</head>
<body>
<div class="page">

  <!-- header -->
  <div class="abs brand"><span class="brand-mark"></span><span>Kestrel<br>Legal<br>Partners</span></div>

  <svg class="abs clock-icon" width="24" height="28" viewBox="0 0 24 28" aria-hidden="true">
    <circle cx="12" cy="15" r="9" fill="none" stroke="#34a3dc" stroke-width="2"/>
    <path d="M12 9v6l4 2" fill="none" stroke="#34a3dc" stroke-width="2" stroke-linecap="round"/>
    <path d="M3 6l4-3M21 6l-4-3" stroke="#34a3dc" stroke-width="2" stroke-linecap="round"/>
  </svg>
  <svg class="abs brace" width="10" height="46" viewBox="0 0 10 46" aria-hidden="true">
    <path d="M9 1C4 1 5 8 5 16s-4 7-4 7 4 0 4 7-1 15 4 15" fill="none" stroke="#34a3dc" stroke-width="1.5"/>
  </svg>
  <div class="abs clocks" style="left:555px">
    <div class="clock-row"><span class="flag" style="background:linear-gradient(90deg,#111 33%,#c8102e 33% 66%,#1a8a3a 66%)"></span><span class="city">KABUL</span><span class="time">MON, DEC 23, 2013 (AFT) 4:20 PM</span></div>
    <div class="clock-row"><span class="flag" style="background:linear-gradient(90deg,#c8102e 30%,transparent 30%),linear-gradient(180deg,#1a8a3a 33%,#fff 33% 66%,#111 66%)"></span><span class="city">DUBAI</span><span class="time">MON, DEC 23, 2013 (GST) 3:15 PM</span></div>
    <div class="clock-row"><span class="flag" style="background:linear-gradient(90deg,#2b3f86 40%,transparent 40%),repeating-linear-gradient(180deg,#c8102e 0 1px,#fff 1px 2px)"></span><span class="city">WASHINGTON</span><span class="time">MON, DEC 23, 2013 (EST) 6:52 AM</span></div>
  </div>
  <div class="abs call">
    <svg width="20" height="20" viewBox="0 0 20 20" aria-hidden="true"><circle cx="10" cy="10" r="10" fill="#8a8a8a"/><path d="M5 8c0-2 2-3 5-3s5 1 5 3l-2 1-1-2H8L7 9zM6 10h8l1 5H5z" fill="#fff"/></svg>
    <span>Call Us At:<strong>(000) 555-0199</strong></span>
  </div>

  <!-- nav -->
  <nav class="abs nav">
    <ul>
      <li class="active">HOME</li><li>PRACTICE AREAS</li><li>WHY CHOOSE US</li><li>FEE STRUCTURE</li><li>GET FREE ADVICE</li><li>CONTACT US</li><li>CLOSING TIPS</li>
    </ul>
  </nav>

  <!-- hero -->
  <div class="abs hero" role="img" aria-label="Photo of a Kabul street with a Ferris wheel, mountains beyond and an Afghan flag in the foreground"></div>
  <div class="abs hero-cta">Learn more about our services</div>
  <div class="abs hero-caption">DEDICATED TO PROVIDING THE HIGHEST QUALITY LEGAL ADVICE AND COUNSELING TO<br>CLIENTS THROUGHOUT KABUL, DUBAI AND WASHINGTON DC</div>
  <svg class="abs hero-arrow" style="left:140px" width="12" height="26" viewBox="0 0 12 26" aria-hidden="true"><path d="M10 1L2 13l8 12" fill="none" stroke="#ddd" stroke-width="1.5"/></svg>
  <svg class="abs hero-arrow" style="left:740px" width="12" height="26" viewBox="0 0 12 26" aria-hidden="true"><path d="M2 1l8 12-8 12" fill="none" stroke="#ddd" stroke-width="1.5"/></svg>

  <!-- welcome -->
  <h2 class="abs section-title welcome-title">Welcome To Kestrel</h2>
  <div class="abs welcome-box">
    <p>Lorem Ipsum is simply dummy text of the printing and typesetting industry. Lorem Ipsum has been the industry's standard dummy text ever since the 1500s, when an unknown printer took a galley of type and scrambled it to make a type specimen book. It has survived not only five centuries, but also the leap into electronic typesetting, remaining essentially unchanged. It was popularised in the 1960s with the release of Letraset sheets containing Lorem Ipsum passages, and more recently with desktop publishing software like Aldus PageMaker including versions of Lorem Ipsum.</p>
    <ul>
      <li><svg width="9" height="9" viewBox="0 0 9 9" aria-hidden="true"><rect x=".5" y=".5" width="8" height="8" fill="none" stroke="#444"/><path d="M2 4.5l2 2 4-5" fill="none" stroke="#444" stroke-width="1.2"/></svg>Provides individualized service that gives its clients confidence and peace of mind.</li>
      <li><svg width="9" height="9" viewBox="0 0 9 9" aria-hidden="true"><rect x=".5" y=".5" width="8" height="8" fill="none" stroke="#444"/><path d="M2 4.5l2 2 4-5" fill="none" stroke="#444" stroke-width="1.2"/></svg>Possesses vast experience and resources that enables it to handle your legal needs in a professional manner with efficiency, clarity, and resolve.</li>
      <li><svg width="9" height="9" viewBox="0 0 9 9" aria-hidden="true"><rect x=".5" y=".5" width="8" height="8" fill="none" stroke="#444"/><path d="M2 4.5l2 2 4-5" fill="none" stroke="#444" stroke-width="1.2"/></svg>Charges reasonable and straight-forward prices for the legal services rendered.</li>
    </ul>
  </div>

  <h2 class="abs section-title locations-title">Our Locations &amp; Offices</h2>
  <div class="abs office">
    <h3>Kabul Office</h3>
    <p>418 Garden Lane, 3rd Floor,<br>Kabul, District 4, 10021,<br>(111)-555-0142</p>
    <div class="pager">
      <svg width="15" height="15" viewBox="0 0 15 15" aria-hidden="true"><circle cx="7.5" cy="7.5" r="7.5" fill="#666"/><path d="M9 4L5.5 7.5 9 11" fill="none" stroke="#222" stroke-width="1.6"/></svg>
      <svg width="15" height="15" viewBox="0 0 15 15" aria-hidden="true"><circle cx="7.5" cy="7.5" r="7.5" fill="#666"/><path d="M6 4l3.5 3.5L6 11" fill="none" stroke="#222" stroke-width="1.6"/></svg>
    </div>
  </div>
  <div class="abs news"><h3>Fresh News</h3><span>CLICK TO VIEW</span></div>

  <!-- practice areas -->
  <div class="abs practice"></div>
  <h2 class="abs section-title practice-title">Our Practice Areas</h2>

  <div class="abs card" style="left:167px"><h4>Business Law</h4><p>Lorem Ipsum is simply dummy text of the printing and typesetting industry. Lorem Ipsum has been the industry's standard dummy text ever since the 1500s</p></div>
  <div class="abs card" style="left:307px"><h4>Internet Law</h4><p>Lorem Ipsum is simply dummy text of the printing and typesetting industry. Lorem Ipsum has been the industry's standard dummy text ever since the 1500s</p></div>
  <div class="abs card" style="left:447px"><h4>Real Estate Law</h4><p>Lorem Ipsum is simply dummy text of the printing and typesetting industry. Lorem Ipsum has been the industry's standard dummy text ever since the 1500s</p></div>
  <div class="abs card" style="left:587px"><h4>Lorem Ipsum Law</h4><p>Lorem Ipsum is simply dummy text of the printing and typesetting industry. Lorem Ipsum has been the industry's standard dummy text ever since the 1500s</p></div>

  <svg class="abs card-icon" style="left:197px" viewBox="0 0 76 76" aria-hidden="true"><circle cx="38" cy="38" r="38" fill="#fff"/><circle cx="38" cy="38" r="30" fill="#34a3dc"/><rect x="25" y="31" width="26" height="18" rx="2" fill="none" stroke="#fff" stroke-width="2.5"/><path d="M33 31v-4h10v4M31 31v18M45 31v18" fill="none" stroke="#fff" stroke-width="2"/></svg>
  <svg class="abs card-icon" style="left:337px" viewBox="0 0 76 76" aria-hidden="true"><circle cx="38" cy="38" r="38" fill="#fff"/><circle cx="38" cy="38" r="30" fill="#34a3dc"/><g transform="rotate(-35 40 42)"><rect x="33" y="32" width="14" height="22" rx="7" fill="none" stroke="#fff" stroke-width="2.2"/><path d="M40 32v7" stroke="#fff" stroke-width="2"/></g><path d="M33 33c-3-4-6-6-9-4" fill="none" stroke="#fff" stroke-width="2"/></svg>
  <svg class="abs card-icon" style="left:477px" viewBox="0 0 76 76" aria-hidden="true"><circle cx="38" cy="38" r="38" fill="#fff"/><circle cx="38" cy="38" r="30" fill="#34a3dc"/><rect x="29" y="24" width="13" height="28" fill="#fff"/><rect x="42" y="33" width="8" height="19" fill="#fff"/><g fill="#34a3dc"><rect x="32" y="28" width="3" height="3"/><rect x="37" y="28" width="3" height="3"/><rect x="32" y="34" width="3" height="3"/><rect x="37" y="34" width="3" height="3"/><rect x="32" y="40" width="3" height="3"/><rect x="37" y="40" width="3" height="3"/><rect x="44" y="37" width="3" height="3"/><rect x="44" y="43" width="3" height="3"/></g></svg>
  <svg class="abs card-icon" style="left:617px" viewBox="0 0 76 76" aria-hidden="true"><circle cx="38" cy="38" r="38" fill="#fff"/><circle cx="38" cy="38" r="30" fill="#34a3dc"/><path d="M24 32l14-8 14 8z" fill="#fff"/><rect x="24" y="48" width="28" height="3" fill="#fff"/><g fill="#fff"><rect x="27" y="34" width="3" height="12"/><rect x="33" y="34" width="3" height="12"/><rect x="40" y="34" width="3" height="12"/><rect x="46" y="34" width="3" height="12"/></g></svg>

  <div class="abs more" style="left:242px">Read more ›</div>
  <div class="abs more" style="left:382px">Read more ›</div>
  <div class="abs more" style="left:522px">Read more ›</div>
  <div class="abs more" style="left:662px">Read more ›</div>

  <!-- testimonials -->
  <h2 class="abs section-title testi-title">Testimonials</h2>
  <div class="abs testi"></div>
  <div class="abs testi-quote">“</div>
  <div class="abs testi-body">
    <p>Lorem Ipsum is simply dummy text of the printing and typesetting industry.<br>Lorem Ipsum has been the industry's standard dummy text ever since the 1500s</p>
    <p class="by">Thanks Guys</p>
    <p class="name">Dara Whitlow, Some Country</p>
  </div>
  <div class="abs testi-side">If you need representation in any area of law not listed above, please <a>contact us</a>. We have many experienced attorneys that we work with and we will be happy to refer you to an attorney who can handle your matter.</div>

  <!-- footer -->
  <div class="abs foot-nav">
    <ul><li>Home</li><li>Practice areas</li><li>Why Choose Us</li><li>Fee Structure</li><li>Get Free Advice</li><li>Contact Us</li><li>Closing Tips</li></ul>
  </div>
  <div class="abs social"><span></span><span></span><span></span></div>
  <div class="abs footer"></div>
  <div class="abs legal">Disclaimer &nbsp;/&nbsp; Privacy Policy &nbsp;/&nbsp; Site Map &nbsp;/&nbsp; Languages</div>
  <p class="abs copy">© 2013 Afghan legal and government relations advisory firm , All Rights Reserved. Our attorneys provide legal services througt New York City (Brooklyn, Dubai, Afganistan and Washington DC</p>

</div>
</body>
</html>
```